Verdano Harvest - Stationery Design Project

We need a stationary for our business. We grow roots and fruits in Central and South America, we import and distribute in FL, USA. We do fresh and frozen products.

Target Market(s)

Small and big supermarkets, wholesalers, traders, distributors, etc

Industry/Entity Type

Business

```html
<!DOCTYPE html>
<html lang="en">
<head>
<meta charset="utf-8">
<title>Verdano Harvest – Stationery</title>
<link rel="stylesheet" href="https://fonts.googleapis.com/css2?family=Montserrat:wght@500&family=Open+Sans:wght@400;600&family=Tinos:ital@0;1&display=swap">
<style>
  :root {
    --leaf-green: #586638;
    --harvest-orange: #e8850f;
    --soft-orange: #f6c98f;
    --paper: #ffffff;
    --ink: #1a1a1a;
    --backdrop: #ebebeb;
  }
  * { box-sizing: border-box; margin: 0; padding: 0; }
  html, body { width: 1200px; height: 1000px; overflow: hidden; }
  body {
    position: relative;
    background: var(--backdrop);
    font-family: "Open Sans", Arial, sans-serif;
  }

  .brand {
    font-family: "Montserrat", Arial, sans-serif;
    font-weight: 500;
    color: var(--harvest-orange);
    letter-spacing: 0.02em;
    white-space: nowrap;
    display: flex;
    align-items: center;
    gap: 6px;
  }
  .brand-dot {
    display: inline-block;
    border-radius: 50%;
    background: var(--leaf-green);
  }

  /* Letterhead */
  .letterhead {
    position: absolute;
    left: 85px; top: 75px;
    width: 602px; height: 850px;
    background: var(--paper);
    overflow: hidden;
  }
  .letterhead .brand {
    position: absolute;
    left: 0; right: 0; top: 62px;
    justify-content: center;
    font-size: 19px;
  }
  .letterhead .brand-dot { width: 9px; height: 9px; }
  .letter-body {
    position: absolute;
    left: 78px; top: 193px;
    width: 449px;
    font-family: "Tinos", "Times New Roman", serif;
    font-size: 12.4px;
    line-height: 15.5px;
    color: var(--ink);
  }
  .letter-body p { text-align: justify; margin-bottom: 15.5px; }
  .letter-closing { margin-top: 47px; text-align: left !important; }
  .signature-mark {
    width: 110px; height: 34px;
    margin: 4px 0 2px;
    background: linear-gradient(90deg, #d9d9d9, #efefef);
    border-radius: 3px;
  }
  .letter-signer { margin-bottom: 0 !important; text-align: left !important; }

  .letter-footer { position: absolute; left: 0; bottom: 0; width: 602px; height: 125px; }
  .letter-contact {
    position: absolute;
    left: 384px; top: 786px;
    color: #fff;
    font-size: 7.2px;
    line-height: 12px;
    white-space: nowrap;
  }
  .contact-grid { display: grid; grid-template-columns: 95px auto; margin-top: 4px; }
  .contact-item { display: flex; align-items: center; gap: 8px; }
  .icon { width: 8px; height: 8px; flex: none; }

  /* Business card front */
  .card-front {
    position: absolute;
    left: 722px; top: 74px;
    width: 388px; height: 215px;
    background: var(--leaf-green);
    text-align: center;
  }
  .card-front .brand {
    position: absolute; left: 0; right: 0; top: 82px;
    justify-content: center;
    font-size: 27px;
  }
  .card-front .brand-dot { width: 12px; height: 12px; background: #fff; }
  .card-url {
    position: absolute; left: 0; right: 0; top: 132px;
    color: #fff; font-size: 12.5px; letter-spacing: 0.02em;
  }
  .card-url span { color: var(--harvest-orange); }

  /* Business card back */
  .card-back {
    position: absolute;
    left: 722px; top: 318px;
    width: 388px; height: 215px;
    background: var(--paper);
    overflow: hidden;
  }
  .card-back .brand {
    position: absolute; left: 28px; top: 40px;
    font-size: 19px;
  }
  .card-back .brand-dot { width: 9px; height: 9px; }
  .card-wave { position: absolute; left: 0; top: 0; }
  .card-holder { position: absolute; left: 33px; top: 159px; color: #fff; }
  .card-holder-name { font-size: 13.5px; letter-spacing: 0.02em; }
  .card-holder-role { font-size: 6.5px; color: var(--harvest-orange); margin-top: 4px; }
  .card-contact {
    position: absolute; right: 21px; top: 124px;
    color: #fff; font-size: 7.2px; line-height: 15px;
    text-align: right;
    white-space: nowrap;
  }
  .card-contact .contact-item { justify-content: flex-end; }
  .card-contact .address { margin-bottom: 5px; }
</style>
</head>
<body>

<article class="letterhead">
  <div class="brand">Verdano Harvest <span class="brand-dot"></span></div>

  <div class="letter-body">
    <p>Gentlemen,</p>
    <p>Enclosed I have the honor to send you an article which I should be pleased if you would accept for the "Meridian Quarterly". I am <em>desperately</em> pushed for money; and in the event of Mr. Harlow's liking the "Landscape-Garden", I would take it as an especial favor if you would mail me the amount due for it, so as to reach me here by the 21st, on which day I shall need it. Can you possibly oblige me in this? If you accept the paper I presume you will allow me your usual sum, whatever that is for similar contributions—but I set no price—leaving all to your own liberality. The piece will make 8 of your pages and rather more.</p>
    <p>Will you be kind enough to put the best possible interpretation upon my behavior while in N-York? You must have conceived a <em>queer</em> idea of me—but the simple truth is that Pemberton would insist upon <em>the juleps</em>, and I knew not what I was either doing or saying. The Review of Ashby which I offered you was deficient in a 1/2 page of commencement, which I had written to supersede the old beginning, and which gave the article the character of a general and retrospective review. No wonder you did not take it—I would have been very much mortified if you had. I hope to see you at some future time, under better auspices.</p>
    <p class="letter-closing">In the meantime I remain<br>Yours very truly,</p>
    <div class="signature-mark" role="img" aria-label="Handwritten signature"></div>
    <p class="letter-signer">Elias Thorne</p>
  </div>

  <svg class="letter-footer" viewBox="0 0 602 125" aria-hidden="true">
    <path d="M0,20 C120,60 180,100 260,90 C320,80 340,20 602,6 L602,125 L0,125Z" fill="var(--soft-orange)"/>
    <path d="M0,26 C120,66 180,106 260,96 C320,86 340,26 602,12 L602,125 L0,125Z" fill="var(--harvest-orange)"/>
    <path d="M0,30 C120,70 180,110 260,100 C320,90 340,30 602,16 L602,125 L0,125Z" fill="var(--leaf-green)"/>
  </svg>

  <div class="letter-contact">
    <div>#14 Palm Grove Road, Tampa, FL 33602, USA</div>
    <div class="contact-grid">
      <div class="contact-item"><svg class="icon" viewBox="0 0 8 8"><rect x="2" y="0.5" width="4" height="7" rx="0.8" fill="none" stroke="var(--harvest-orange)"/></svg>+1 813 555 0142</div>
      <div class="contact-item"><svg class="icon" viewBox="0 0 8 8"><rect x="0.5" y="3" width="7" height="4" fill="none" stroke="var(--harvest-orange)"/><rect x="2" y="0.5" width="4" height="2.5" fill="var(--harvest-orange)"/></svg>+1 813 555 0176</div>
      <div class="contact-item"><svg class="icon" viewBox="0 0 8 8"><path d="M0.5,3 C2,1 6,1 7.5,3 L6.5,4 L5.5,3 L2.5,3 L1.5,4Z M1.5,5 H6.5 V7.5 H1.5Z" fill="var(--harvest-orange)"/></svg>+1 813 555 0177</div>
      <div class="contact-item"><svg class="icon" viewBox="0 0 8 8"><rect x="0.5" y="1.5" width="7" height="5" fill="none" stroke="var(--harvest-orange)"/><path d="M0.5,1.5 L4,4.5 L7.5,1.5" fill="none" stroke="var(--harvest-orange)"/></svg>sales@verdanoharvest.com</div>
    </div>
  </div>
</article>

<section class="card-front">
  <div class="brand">Verdano Harvest <span class="brand-dot"></span></div>
  <div class="card-url">www.<span>verdanoharvest</span>.com</div>
</section>

<section class="card-back">
  <svg class="card-wave" width="388" height="215" viewBox="0 0 388 215" aria-hidden="true">
    <path d="M0,80 C60,112 110,126 180,96 C250,66 310,47 388,54 L388,215 L0,215Z" fill="var(--soft-orange)"/>
    <path d="M0,88 C60,120 110,134 180,104 C250,74 310,55 388,62 L388,215 L0,215Z" fill="var(--harvest-orange)"/>
    <path d="M0,94 C60,126 110,140 180,110 C250,80 310,62 388,69 L388,215 L0,215Z" fill="var(--leaf-green)"/>
  </svg>
  <div class="brand">Verdano Harvest <span class="brand-dot"></span></div>

  <div class="card-holder">
    <div class="card-holder-name">Marco Ruiz</div>
    <div class="card-holder-role">CEO</div>
  </div>

  <div class="card-contact">
    <div class="address">#14 Palm Grove Road, Tampa, FL 33602, USA</div>
    <div class="contact-item">+1 813 555 0142 <svg class="icon" viewBox="0 0 8 8"><rect x="2" y="0.5" width="4" height="7" rx="0.8" fill="none" stroke="var(--harvest-orange)"/></svg></div>
    <div class="contact-item">+1 813 555 0177 <svg class="icon" viewBox="0 0 8 8"><path d="M0.5,3 C2,1 6,1 7.5,3 L6.5,4 L5.5,3 L2.5,3 L1.5,4Z M1.5,5 H6.5 V7.5 H1.5Z" fill="var(--harvest-orange)"/></svg></div>
    <div class="contact-item">+1 813 555 0176 <svg class="icon" viewBox="0 0 8 8"><rect x="0.5" y="3" width="7" height="4" fill="none" stroke="var(--harvest-orange)"/><rect x="2" y="0.5" width="4" height="2.5" fill="var(--harvest-orange)"/></svg></div>
    <div class="contact-item">sales@verdanoharvest.com <svg class="icon" viewBox="0 0 8 8"><rect x="0.5" y="1.5" width="7" height="5" fill="none" stroke="var(--harvest-orange)"/><path d="M0.5,1.5 L4,4.5 L7.5,1.5" fill="none" stroke="var(--harvest-orange)"/></svg></div>
  </div>
</section>

</body>
</html>
```